Banner Ad Design Project

I need a banner design. The website is under construction at www.brightmarrow.example

Name: Bright Marrow
Tagline: Steady Sparks for crowded calendars

This is a leadership development and executive coaching site. The past site is live at www.quillstepnow.example. (so you can get a sense of the content)

The audience are (BUSY) executives, senior managers, leaders and top professionals, so the feel needs to be highly professional but also modern and fresh. I want to communicate energy but also solid and trust worthy and not too new agey. The audience are also people with strong social values who want to change things - so not too corporate (Ie suits!)

I would like the design to be floating on a white background, very clean and simple. I am attracted to reds or sunset (burn orange crimson colors.) But totally open to any color ideas.
I am giving an open brief for your ideas.
Here are the dimensions 960px wide, roughly 190px height.

Reason: The weekend might give more time to designers to get involved. Thanks Vina

Hi designers

You may not have seen the additions I gave to this brief.

The banner should not have leader out front photo's. Maybe less corporate than I initially thought. 
Not too corporate (no suits!) Please no chess pieces, jigsaw pieces, cartoon images, cliche leadership images. 
Am am trying for inspiration /inspiring whilst still being professional. Very simple and clean.
Please can the design be floating in a white background so that the web page is borderless - A bit like it is in http://palmoriskel.example/
Thank you

Target Market(s)

Senior managers, executives but people who also want to change the world!

Industry/Entity Type

Construction

Requirements
Should not have
• Should not have leader out front photo's.
Maybe less corporate than I initially thought.
Am am trying for inspiration /inspiring whilst still being professional.
Please no chess pieces, jigsaw pieces, cartoon images, cliche leadership images. Not too corporate (Ie suits!)

Thanks

```html
<!DOCTYPE html>
<html lang="en">
<head>
<meta charset="utf-8">
<title>Practical inspiration for people leading change</title>
<link rel="stylesheet" href="https://fonts.googleapis.com/css2?family=Orbitron:wght@700;800&display=swap">
<style>
  :root {
    --paper: #ffffff;
    --ring-red: #ff5a0a;
    --ring-orange: #ff9a0a;
    --photo-warm: #e9b43c;
    --photo-deep: #7a2a14;
    --title-light: #ffb21a;
    --title-deep: #ff7a00;
    --tagline: #e0820a;
    --outline: #3a1c08;
    --leaf-haze: #cfe0f7;
  }
  html, body {
    margin: 0;
    padding: 0;
    width: 1200px;
    height: 238px;
    overflow: hidden;
    background: var(--paper);
  }
  .banner {
    position: relative;
    width: 1200px;
    height: 238px;
    background: var(--paper);
    overflow: hidden;
  }
  .banner svg {
    position: absolute;
    inset: 0;
    display: block;
  }
  .headline {
    font-family: "Orbitron", sans-serif;
    font-weight: 800;
    paint-order: stroke fill;
    stroke: var(--outline);
    stroke-linejoin: round;
  }
  .headline__title {
    fill: url(#titleFill);
    stroke-width: 3px;
  }
  .headline__tagline {
    font-weight: 700;
    fill: var(--tagline);
    stroke-width: 2.5px;
  }
</style>
</head>
<body>
<div class="banner">
  <svg width="1200" height="238" viewBox="0 0 1200 238" xmlns="http://www.w3.org/2000/svg">
    <defs>
      <linearGradient id="titleFill" x1="0" y1="0" x2="0" y2="1">
        <stop offset="0" stop-color="var(--title-light)"/>
        <stop offset="1" stop-color="var(--title-deep)"/>
      </linearGradient>
      <linearGradient id="photoTone" x1="0" y1="0" x2="0" y2="1">
        <stop offset="0" stop-color="var(--photo-warm)"/>
        <stop offset="0.7" stop-color="#d08a3a"/>
        <stop offset="1" stop-color="var(--photo-deep)"/>
      </linearGradient>
      <radialGradient id="leafHaze" cx="0.75" cy="0.6" r="0.6">
        <stop offset="0" stop-color="var(--leaf-haze)" stop-opacity="0.55"/>
        <stop offset="1" stop-color="var(--leaf-haze)" stop-opacity="0"/>
      </radialGradient>
    </defs>

    <rect class="leaf-backdrop" x="280" y="0" width="920" height="238" fill="url(#leafHaze)"
          role="img" aria-label="Faint pale blue scattered leaf pattern"/>

    <g class="emblem">
      <circle class="emblem__ring-red" cx="88" cy="119" r="227" fill="var(--ring-red)"/>
      <circle class="emblem__gap" cx="88" cy="119" r="187" fill="var(--paper)"/>
      <circle class="emblem__ring-orange" cx="88" cy="119" r="181" fill="var(--ring-orange)"/>
      <circle class="emblem__inner-frame" cx="88" cy="119" r="106" fill="var(--paper)"/>
      <circle class="emblem__photo" cx="88" cy="119" r="100" fill="url(#photoTone)"
              role="img" aria-label="Photo of a person seated, hands covering their eyes"/>
    </g>

    <g class="headline">
      <text class="headline__title" x="340" y="106" textLength="829" lengthAdjust="spacingAndGlyphs"><tspan font-size="68">P</tspan><tspan font-size="50">RACTICAL INSPIRATION</tspan></text>
      <text class="headline__tagline" x="431" y="168" font-size="38" textLength="644" lengthAdjust="spacingAndGlyphs">FOR PEOPLE LEADING CHANGE</text>
    </g>
  </svg>
</div>
</body>
</html>
```